Quelmira Business Card

Need a business card for our business.

Attached are our Logos. There is either the white and black all the all red with white. Either Logo can be used.

The winner will be provided the details for phone number and address.

Good Luck!

Business

```html
<!DOCTYPE html>
<html lang="en">
<head>
<meta charset="utf-8">
<title>Quelmira Business Card</title>
<link rel="stylesheet" href="https://fonts.googleapis.com/css2?family=Open+Sans:wght@400;600;700;800&display=swap">
<style>
  :root {
    --backdrop: #e6e1da;
    --card-white: #ffffff;
    --card-dark: #141618;
    --card-dark-edge: #0a0b0c;
    --brand-red: #8f1c22;
    --brand-red-deep: #4a1417;
    --brand-red-mid: #7a2229;
    --text-light: #f2f2f2;
    --divider: #5a5d60;
  }
  * { margin: 0; padding: 0; box-sizing: border-box; }
  html, body {
    width: 1200px; height: 899px; overflow: hidden;
    background: var(--backdrop);
    font-family: "Open Sans", Arial, sans-serif;
  }
  .canvas { position: relative; width: 1200px; height: 899px; }

  .card {
    position: absolute; width: 614px; height: 349px; overflow: hidden;
    box-shadow: 2px 3px 6px rgba(0,0,0,0.35);
  }

  /* Front */
  .card-front { left: 97px; top: 97px; background: var(--card-white); }
  .front-top {
    position: absolute; left: 0; top: 0; width: 100%; height: 172px;
    background: var(--card-white);
    display: flex; align-items: center; justify-content: center;
  }
  .accent-stripe {
    position: absolute; left: 0; top: 172px; width: 100%; height: 5px;
    background: var(--brand-red);
  }
  .front-bottom {
    position: absolute; left: 0; top: 177px; width: 100%; height: 172px;
    background: radial-gradient(ellipse at 50% 30%, #26292c 0%, var(--card-dark) 55%, var(--card-dark-edge) 100%);
  }
  .wordmark {
    font-weight: 800; letter-spacing: -1px; line-height: 1;
  }
  .front-top .wordmark { font-size: 52px; color: var(--brand-red); }

  .person {
    position: absolute; right: 346px; top: 68px; text-align: right; color: var(--text-light);
  }
  .person-name { font-size: 25px; font-weight: 400; line-height: 1.1; }
  .person-role { font-size: 17px; font-weight: 400; line-height: 1.3; }

  .divider {
    position: absolute; left: 304px; top: 15px; width: 2px; height: 137px;
    background: linear-gradient(to bottom, transparent, var(--divider) 20%, var(--divider) 80%, transparent);
  }

  .contact-list { position: absolute; left: 332px; top: 28px; list-style: none; }
  .contact-item {
    display: flex; align-items: center; height: 32px;
    color: var(--text-light); font-size: 13px;
  }
  .contact-icon { width: 20px; height: 20px; margin-right: 8px; fill: none; stroke: var(--text-light); stroke-width: 1.4; }
  .contact-icon .solid { fill: var(--text-light); stroke: none; }

  /* Back */
  .card-back {
    left: 494px; top: 466px;
    background: radial-gradient(ellipse at 50% 65%, #872a32 0%, var(--brand-red-mid) 35%, var(--brand-red-deep) 100%);
    display: flex; align-items: center; justify-content: center;
  }
  .card-back .wordmark { font-size: 56px; color: var(--card-white); margin-top: -20px; }
  .back-url {
    position: absolute; left: 0; width: 100%; top: 313px; text-align: center;
    color: var(--text-light); font-size: 12px; font-weight: 600;
  }
</style>
</head>
<body>
<main class="canvas">
  <section class="card card-front" aria-label="Business card front">
    <div class="front-top"><span class="wordmark">QUELMIRA</span></div>
    <div class="accent-stripe"></div>
    <div class="front-bottom">
      <div class="person">
        <div class="person-name">Daniel Hart</div>
        <div class="person-role">Director</div>
      </div>
      <div class="divider"></div>
      <ul class="contact-list">
        <li class="contact-item">
          <svg class="contact-icon" viewBox="0 0 20 20" aria-hidden="true"><rect x="6" y="2" width="8" height="16" rx="1"/><line x1="7" y1="14" x2="13" y2="14"/></svg>
          +01.555.204.318
        </li>
        <li class="contact-item">
          <svg class="contact-icon" viewBox="0 0 20 20" aria-hidden="true"><path class="solid" d="M5 2l3 3-1.5 2.5c1 2.5 3 4.5 5.5 5.5L14.5 11.5l3 3-2 3c-6 0-12-6-12.5-12.5z"/></svg>
          +01.555.730.462
        </li>
        <li class="contact-item">
          <svg class="contact-icon" viewBox="0 0 20 20" aria-hidden="true"><rect x="2" y="5" width="16" height="10"/><polyline points="2,5 10,11 18,5"/></svg>
          d_hart@quelmira.com
        </li>
        <li class="contact-item">
          <svg class="contact-icon" viewBox="0 0 20 20" aria-hidden="true"><circle cx="10" cy="10" r="8"/><ellipse cx="10" cy="10" rx="3.5" ry="8"/><line x1="2" y1="10" x2="18" y2="10"/><line x1="3.5" y1="6" x2="16.5" y2="6"/><line x1="3.5" y1="14" x2="16.5" y2="14"/></svg>
          www.quelmira.com
        </li>
      </ul>
    </div>
  </section>

  <section class="card card-back" aria-label="Business card back">
    <span class="wordmark">QUELMIRA</span>
    <div class="back-url">www.quelmira.com</div>
  </section>
</main>
</body>
</html>
```